Bright Path Therapies business cards and stationary

Need business cards and stationary designed to match previously made logo for for a new company based in Sydney NSW called 'Bright Path Therapies'.

We provide early intervention services and diagnostic assessment for children with disability and their families. I would like designs that are colourful and child friendly - possibly using feet/footprints/steps on a white background. The final design should communicate that we are family friendly, accepting and fun to work with.

Target Market(s)

Parents and Families
Teachers
Allied Health Professionals

Industry/Entity Type

Psychology

Contact Information for Business Card

Bright Path Therapies
www.brightpaththerapies.example
info@brightpaththerapies.example

Font styles to use
Sans Serif
Decorative
Script

Requirements
Must have
• Match the font and colour scheme of logo, along with footprint picture
Nice to have
• Clean and simple, while reflecting that I am working with families.
• Also- editable for when we make staff specific cards.

```html
<!DOCTYPE html>
<html lang="en">
<head>
<meta charset="utf-8">
<title>Bright Path Therapies – Business Card</title>
<link rel="stylesheet" href="https://fonts.googleapis.com/css2?family=Montserrat:wght@500;600;800&family=Roboto:wght@400;500&display=swap">
<style>
  :root {
    --bg: #e9e9ec;
    --white: #ffffff;
    --red: #ec3b3b;
    --orange: #f7941d;
    --blue: #1f78c8;
    --green: #8cc63f;
    --grey-text: #555a66;
    --print-shade: #eef0f8;
  }
  * { box-sizing: border-box; margin: 0; padding: 0; }
  html, body { width: 1200px; height: 900px; overflow: hidden; }
  body {
    background: var(--bg);
    position: relative;
    font-family: "Montserrat", sans-serif;
  }
  .card {
    position: absolute;
    left: 240px;
    width: 720px;
    height: 410px;
    border-radius: 26px;
    overflow: hidden;
    box-shadow: 0 6px 18px rgba(0,0,0,0.18);
  }

  /* Back of card */
  .card--back {
    top: 30px;
    background: linear-gradient(to top, var(--red) 0%, var(--orange) 48%, var(--blue) 100%);
  }
  .card--back .footprint-trail {
    position: absolute;
    right: 40px;
    top: 60px;
    width: 170px;
    height: 320px;
    border-radius: 60px;
    background: linear-gradient(to bottom, rgba(255,255,255,0.16), rgba(255,255,255,0.08));
  }
  .card--back .brand {
    position: absolute;
    left: 0; right: 0;
    top: 140px;
    display: flex;
    justify-content: center;
    align-items: center;
    gap: 18px;
  }
  .card--back .brand-dot {
    width: 78px; height: 78px;
    border-radius: 50%;
    background: var(--white);
  }
  .card--back .brand-name {
    font-weight: 600;
    font-size: 40px;
    color: var(--white);
    letter-spacing: 0.5px;
  }
  .card--back .website {
    position: absolute;
    left: 0; right: 0;
    bottom: 70px;
    text-align: center;
    font-family: "Roboto", sans-serif;
    font-weight: 500;
    font-size: 22px;
    color: var(--white);
    letter-spacing: 0.3px;
  }

  /* Front of card */
  .card--front {
    top: 470px;
    background: var(--white);
  }
  .card--front .footprint-trail {
    position: absolute;
    right: 70px;
    top: 50px;
    width: 210px;
    height: 300px;
    border-radius: 70px;
    background: var(--print-shade);
  }
  .card--front .brand {
    position: absolute;
    left: 44px;
    top: 90px;
    display: flex;
    align-items: center;
    gap: 14px;
  }
  .card--front .brand-dot {
    width: 62px; height: 62px;
    border-radius: 50%;
    background: var(--red);
  }
  .card--front .brand-name {
    font-weight: 600;
    font-size: 27px;
    color: var(--blue);
    line-height: 1.15;
    width: 190px;
  }
  .divider {
    position: absolute;
    left: 330px;
    top: 80px;
    width: 2px;
    height: 100px;
    background: var(--blue);
  }
  .person {
    position: absolute;
    left: 360px;
    top: 100px;
  }
  .person-name {
    font-weight: 800;
    font-size: 36px;
    letter-spacing: 1px;
    color: var(--blue);
  }
  .person-name .surname { color: var(--red); }
  .person-role {
    margin-top: 4px;
    font-weight: 600;
    font-size: 16px;
    letter-spacing: 1.5px;
    color: var(--orange);
  }
  .contact-band {
    position: absolute;
    left: 0; right: 0; bottom: 0;
    height: 110px;
    background: linear-gradient(to right, var(--green) 0%, var(--red) 14%, var(--orange) 45%, #8a8aa0 70%, var(--blue) 90%);
    display: flex;
    flex-direction: column;
    justify-content: center;
    gap: 14px;
    padding-left: 44px;
  }
  .contact-line {
    display: flex;
    align-items: center;
    gap: 14px;
    font-family: "Roboto", sans-serif;
    font-weight: 500;
    font-size: 20px;
    color: var(--white);
  }
  .contact-icon {
    width: 32px; height: 32px;
    border-radius: 50%;
    background: var(--white);
    display: flex;
    align-items: center;
    justify-content: center;
    flex-shrink: 0;
  }
</style>
</head>
<body>

  <section class="card card--back">
    <div class="footprint-trail" role="img" aria-label="Faint trail of footprints"></div>
    <div class="brand">
      <span class="brand-dot"></span>
      <span class="brand-name">Bright Path Therapies</span>
    </div>
    <p class="website">www.brightpaththerapies.example</p>
  </section>

  <section class="card card--front">
    <div class="footprint-trail" role="img" aria-label="Faint trail of footprints"></div>
    <div class="brand">
      <span class="brand-dot"></span>
      <span class="brand-name">Bright Path Therapies</span>
    </div>
    <span class="divider"></span>
    <div class="person">
      <p class="person-name">MAYA <span class="surname">COLLINS</span></p>
      <p class="person-role">MANAGING DIRECTOR</p>
    </div>
    <div class="contact-band">
      <p class="contact-line">
        <span class="contact-icon">
          <svg width="18" height="18" viewBox="0 0 24 24" aria-hidden="true">
            <path fill="#f7941d" d="M6.6 10.8a15.1 15.1 0 0 0 6.6 6.6l2.2-2.2a1 1 0 0 1 1-.25 11.4 11.4 0 0 0 3.6.57 1 1 0 0 1 1 1V20a1 1 0 0 1-1 1A17 17 0 0 1 3 4a1 1 0 0 1 1-1h3.5a1 1 0 0 1 1 1c0 1.25.2 2.45.57 3.57a1 1 0 0 1-.25 1z"/>
          </svg>
        </span>
        0400-123-456
      </p>
      <p class="contact-line">
        <span class="contact-icon">
          <svg width="18" height="18" viewBox="0 0 24 24" aria-hidden="true">
            <rect x="3" y="6" width="18" height="12" rx="1.5" fill="none" stroke="#f7941d" stroke-width="2"/>
            <path d="M3.5 7l8.5 6 8.5-6" fill="none" stroke="#f7941d" stroke-width="2"/>
          </svg>
        </span>
        info@brightpaththerapies.example
      </p>
    </div>
  </section>

</body>
</html>
```